Business cards

Design business cards for our company. Just a straight, business like design with the logo, name, function and contact details

Target Market(s)

We are a innovative technological company active in water treatment

Industry/Entity Type

Water management

Contact Information for Business Card

Name, Function, email, telephone number, link to website

```html
<!DOCTYPE html>
<html lang="en">
<head>
<meta charset="utf-8">
<title>Neridawave Business Cards</title>
<link rel="stylesheet" href="https://fonts.googleapis.com/css2?family=Lato:wght@400;700&display=swap">
<style>
  :root {
    --stage: #1f2022;
    --card: #3b3c3e;
    --accent: #2a9be0;
    --muted: #a9aaac;
    --light: #c9cacc;
    --glyph: #3b3c3e;
  }
  * { box-sizing: border-box; margin: 0; padding: 0; }
  html, body {
    width: 1200px; height: 952px; overflow: hidden;
    background: var(--stage);
    font-family: "Lato", sans-serif;
  }
  .sheet {
    width: 1200px; height: 952px;
    display: flex; align-items: center; justify-content: center; gap: 40px;
  }
  .card {
    position: relative;
    width: 540px; height: 309px;
    background: var(--card);
    border-radius: 22px;
    overflow: hidden;
  }
  /* Front */
  .card-front {
    display: flex; align-items: center; justify-content: center; gap: 16px;
  }
  .brand {
    color: var(--accent);
    font-weight: 400;
    letter-spacing: 0.5px;
  }
  .card-front .brand { font-size: 54px; }
  .brand-dot {
    border-radius: 50%;
    background: var(--accent);
    flex: none;
  }
  .card-front .brand-dot { width: 28px; height: 28px; }

  /* Back */
  .holder {
    position: absolute; left: 34px; top: 34px;
  }
  .holder-name {
    color: var(--accent);
    font-size: 19px;
    letter-spacing: 1px;
    text-transform: uppercase;
  }
  .holder-name strong { font-weight: 700; }
  .holder-role {
    color: var(--muted);
    font-size: 12px;
    margin-top: 3px;
  }
  .holder-rule {
    width: 36px; height: 1px; background: var(--muted);
    margin-top: 8px;
  }
  .back-mark {
    position: absolute; right: 34px; top: 112px;
    display: flex; align-items: center; gap: 9px;
  }
  .back-mark .brand { font-size: 26px; }
  .back-mark .brand-dot { width: 14px; height: 14px; }
  .contacts {
    position: absolute; right: 34px; bottom: 28px;
    list-style: none;
    display: flex; flex-direction: column; align-items: flex-end; gap: 7px;
  }
  .contact {
    display: flex; align-items: center; gap: 10px;
    color: var(--light);
    font-size: 12.5px;
    text-align: right;
    line-height: 1.35;
  }
  .contact-icon {
    width: 18px; height: 18px; flex: none;
    background: var(--accent);
    border-radius: 4px;
    display: flex; align-items: center; justify-content: center;
  }
  .contact-icon svg { width: 12px; height: 12px; }
</style>
</head>
<body>
<main class="sheet">
  <section class="card card-back" aria-label="Card back with contact details">
    <div class="holder">
      <h1 class="holder-name">Daniel K. <strong>Hartwell</strong></h1>
      <p class="holder-role">Managing Director</p>
      <div class="holder-rule"></div>
    </div>

    <div class="back-mark">
      <span class="brand">Neridawave</span>
      <span class="brand-dot"></span>
    </div>

    <ul class="contacts">
      <li class="contact">
        <span>2715 Riverside Avenue<br>Portland, OR 97205</span>
        <span class="contact-icon">
          <svg viewBox="0 0 12 12"><path d="M6 1a3.5 3.5 0 0 0-3.5 3.5C2.5 7 6 11 6 11s3.5-4 3.5-6.5A3.5 3.5 0 0 0 6 1zm0 4.8a1.3 1.3 0 1 1 0-2.6 1.3 1.3 0 0 1 0 2.6z" fill="var(--glyph)"/></svg>
        </span>
      </li>
      <li class="contact">
        <span>+00 987 654 32</span>
        <span class="contact-icon">
          <svg viewBox="0 0 12 12"><path d="M3.2 1.2 4.8 3 4 4.4c.6 1.4 1.8 2.6 3.2 3.2L8.6 6.8 10.4 8.4 9.6 10.2C5.4 10.4 1.6 6.6 1.4 2z" fill="var(--glyph)"/></svg>
        </span>
      </li>
      <li class="contact">
        <span>contact@neridawave.com</span>
        <span class="contact-icon">
          <svg viewBox="0 0 12 12"><rect x="1.5" y="3" width="9" height="6.5" rx="0.6" fill="none" stroke="var(--glyph)" stroke-width="1.2"/><path d="M1.8 3.3 6 6.6l4.2-3.3" fill="none" stroke="var(--glyph)" stroke-width="1.2"/></svg>
        </span>
      </li>
      <li class="contact">
        <span>www.neridawave.com</span>
        <span class="contact-icon">
          <svg viewBox="0 0 12 12"><path d="M6 1.2 10 10.5 6 8.3 2 10.5z" fill="var(--glyph)"/></svg>
        </span>
      </li>
    </ul>
  </section>

  <section class="card card-front" aria-label="Card front with company name">
    <span class="brand">Neridawave</span>
    <span class="brand-dot"></span>
  </section>
</main>
</body>
</html>
```